Beauty Salon Design

The business card design will be for a new beauty salon opening up.

The therapist has over 11 years at a leading beauty Salon in perth.

The two colours that the salon will use is black and gold.

Industry/Entity Type

Beauty Salon

Contact Information for Business Card

Velmora Beauty

Corinne Ashdale
Advanced beauty therapist
0457 318 042

Monday - Friday 9am - 2.30pm
Weekends and nights by appointment only

Waxing, Tinting, Swedish massage, hot stone massage, facials, peels, micro, LED light treatment, skin needling and retail products.

```html
<!DOCTYPE html>
<html lang="en">
<head>
<meta charset="utf-8">
<title>Velmora Beauty – Business Card</title>
<link rel="stylesheet" href="https://fonts.googleapis.com/css2?family=Quicksand:wght@300;400&display=swap">
<style>
  :root {
    --stage: #2a2927;
    --card-black: #060606;
    --card-black-edge: #141414;
    --gold: #d9a044;
    --gold-soft: #c99038;
    --photo-hair: #3a2620;
    --photo-skin: #7a5140;
    --photo-skin-light: #a8775c;
    --photo-shadow: #120e0d;
    --photo-backdrop: #4b5157;
    --band-dark: rgba(4, 4, 4, 0.88);
  }
  * { margin: 0; padding: 0; box-sizing: border-box; }
  html, body {
    width: 1200px;
    height: 803px;
    overflow: hidden;
    background: var(--stage);
    font-family: "Quicksand", "Helvetica Neue", Arial, sans-serif;
  }
  .stage {
    position: relative;
    width: 1200px;
    height: 803px;
    display: flex;
    align-items: center;
    justify-content: center;
    gap: 36px;
  }
  .card {
    position: relative;
    width: 564px;
    height: 340px;
    overflow: hidden;
    box-shadow: 0 16px 34px rgba(0, 0, 0, 0.6);
  }

  /* Front: photo side */
  .card--front { background: var(--photo-shadow); }
  .front-photo {
    position: absolute;
    inset: 0;
    background:
      radial-gradient(ellipse 34% 30% at 66% 52%, var(--photo-skin-light) 0%, rgba(168,119,92,0) 100%),
      radial-gradient(ellipse 48% 46% at 60% 50%, var(--photo-skin) 0%, rgba(122,81,64,0) 100%),
      radial-gradient(ellipse 30% 40% at 22% 62%, var(--photo-hair) 0%, rgba(58,38,32,0) 100%),
      linear-gradient(100deg, var(--photo-shadow) 0%, #241a17 38%, #3b3532 70%, var(--photo-backdrop) 100%);
  }
  .services-band {
    position: absolute;
    left: 0; right: 0; bottom: 0;
    height: 104px;
    background: linear-gradient(180deg, rgba(0,0,0,0) 0%, rgba(0,0,0,0.6) 28%, var(--band-dark) 100%);
  }
  .services {
    position: absolute;
    left: 26px;
    right: 22px;
    bottom: 22px;
    text-align: right;
    color: var(--gold);
    font-weight: 400;
    font-size: 16px;
    line-height: 1.5;
  }

  /* Back: details side */
  .card--back {
    background: radial-gradient(ellipse 90% 90% at 70% 30%, var(--card-black-edge) 0%, var(--card-black) 70%);
    color: var(--gold);
    text-align: right;
    padding: 50px 30px 0 30px;
  }
  .brand {
    font-weight: 300;
    font-size: 58px;
    line-height: 1.05;
    color: var(--gold);
  }
  .therapist-name {
    margin-top: 58px;
    font-weight: 300;
    font-size: 27px;
    line-height: 1.2;
    color: var(--gold);
  }
  .details {
    margin-top: 10px;
    font-weight: 400;
    font-size: 16px;
    line-height: 1.5;
    color: var(--gold-soft);
  }
</style>
</head>
<body>
  <main class="stage">
    <section class="card card--front">
      <div class="front-photo" role="img" aria-label="Beauty portrait in profile with dramatic gold and smoky eye make-up against a slate backdrop"></div>
      <div class="services-band"></div>
      <p class="services">Waxing, Tinting, Swedish massage, hot stone massage, facials, peels, micro, LED light treatment, skin needling and retail products.</p>
    </section>

    <section class="card card--back">
      <h1 class="brand">Velmora Beauty</h1>
      <p class="therapist-name">Corinne Ashdale</p>
      <div class="details">
        <p class="role-phone">Advanced beauty therapist ~ 0457 318 042</p>
        <p class="hours">Monday - Friday 9am - 2.30pm</p>
        <p class="hours-note">Weekends and nights by appointment only</p>
      </div>
    </section>
  </main>
</body>
</html>
```